Shopify Design for wedding invitations

We are a greeting card manufactory, special in wedding invitation
I need a shopify website for our wedding invitation brand. (Lovmira), atttach you can find our logo.
We are looking for someone to create a modern and clean looking e-commerce store for our wedding invitation through Shopify. We need some life, professionalism and style put into our site. We will have a variety serie of products : laser cut wedding invitation, popup wedding invitaiton, vintage wedding invitation, handmade wedding invitation, printing invitation, Custom wedding cards, wedding stationery (including favor box, table card, place card, escort card, number card), Thank you card. our online store requires easy navigation to categories divided by product type.

our market is , Eourpe and USA,
please choose a good color for it.
you can go to our website: www.bluestonecraft.com and check our product.
also you can go to Vendoro 4 new items.
https://www.vendoro-shop.com/dp/X47K8Q2M19?ref=abc_item_dp

Target Market(s)

Europe and USA

Industry/Entity Type

wedding

Number of Pages Required

1 page

Requirements
Must have
• Logo, 3 banners than can be changed each 3-5 seconds.
Nice to have
• nice icon and font, beautiful color,

```html
<!DOCTYPE html>
<html lang="en">
<head>
<meta charset="utf-8">
<title>Lovmira – Homepage and Product Category Page</title>
<link href="https://fonts.googleapis.com/css2?family=Inter:wght@300;400;500;600;700&family=Great+Vibes&family=Playfair+Display:wght@700&display=swap" rel="stylesheet">
<style>
:root{
  --stage:#3b3f64;
  --navy:#2c3460;
  --accent:#e0612b;
  --ink:#2a2a2a;
  --line:#e6e6e6;
  --page:#ffffff;
  --soft:#f5f5f5;
  --cream:#fdf6e6;
  --sand:#f8ecd4;
  --butter:#f7e4b4;
  --aqua:#e6f3f6;
  --lilac:#dfe3ef;
  --star:#f2b544;
  --logo:#8a4a2a;
}
*{margin:0;padding:0;box-sizing:border-box}
html,body{width:811px;height:1200px;overflow:hidden;background:var(--stage)}
body{font-family:"Inter",sans-serif;color:var(--ink)}
.stage{position:absolute;left:0;top:0;width:1549px;height:2293px;transform:scale(.5236);transform-origin:0 0;background:var(--stage)}
.stage-title{position:absolute;top:42px;color:#fff;font-size:24px;font-weight:300;letter-spacing:.5px;transform:translateX(-50%)}
.page{position:absolute;background:var(--page);width:720px;overflow:hidden}
.page *{position:absolute}
.page p,.page span{white-space:nowrap}

.logo{top:8px;left:0;width:720px;text-align:center;font-size:20px;font-weight:500;color:var(--logo)}
.nav{top:37px;font-size:9.5px;color:#333}
.nav-caret{display:inline-block;position:static!important;width:0;height:0;border-left:4px solid transparent;border-right:4px solid transparent;border-top:5px solid #222;margin-left:5px;vertical-align:1px}
.search{left:490px;top:36px;width:12px;height:12px}
.search-text{left:510px;top:37px;font-size:9px;color:#aaa}
.hicon{top:36px;width:12px;height:12px}
.header-line{left:0;top:56px;width:720px;height:1px;background:var(--line)}

.hero{left:20px;top:66px;width:680px;height:350px;background:linear-gradient(100deg,#e9e9ea 0%,#d7d7da 35%,#b9b3ad 55%,#2b2b2e 75%,#e7e3de 92%)}
.hero-title{left:70px;top:155px;font-family:"Great Vibes",cursive;font-size:34px;line-height:45px;color:#333;white-space:normal!important;width:290px}
.hero-sub{left:71px;top:252px;font-size:12px;line-height:14px;color:#222;white-space:normal!important;width:260px}
.btn-buy{left:71px;top:291px;width:76px;height:16px;background:var(--navy);color:#fff;font-size:5.5px;text-align:center;line-height:16px}
.arrow{width:18px;height:18px;border-radius:50%;background:#fff}
.arrow::after{content:"";position:absolute;top:5px;border-top:4px solid transparent;border-bottom:4px solid transparent}
.arrow.l::after{left:5px;border-right:6px solid var(--navy)}
.arrow.r::after{left:7px;border-left:6px solid var(--navy)}
.arrow.hot{background:var(--accent)}
.arrow.hot.l::after{border-right-color:#fff}
.arrow.hot.r::after{border-left-color:#fff}
.dot{top:402px;width:6px;height:6px;border-radius:50%;background:#ddd}
.dot.on{background:var(--accent)}

.section-title{left:0;width:720px;text-align:center;font-size:20px;font-weight:300;color:#222}

.chip{width:98px;height:50px;background:#fff;box-shadow:0 1px 4px rgba(0,0,0,.12)}
.chip.on{background:var(--navy)}
.chip-icon{left:8px;top:17px;width:16px;height:14px;border-radius:2px}
.chip-text{left:32px;top:0;height:50px;display:flex;align-items:center;font-size:7px;line-height:8px;color:#333;white-space:normal!important;width:62px}
.chip.on .chip-text{color:#fff}

.coll{top:649px;width:154px;height:194px;background:#f0efee}
.coll-img{left:0;top:0;width:154px;height:130px}
.coll-band{left:0;top:130px;width:154px;height:64px;background:var(--navy)}
.coll-name{left:0;top:16px;width:154px;text-align:center;color:#fff;font-size:12px;font-weight:700}
.coll-link{left:0;top:42px;width:154px;text-align:center;color:#fff;font-size:7.5px;font-weight:600;text-decoration:underline}

.prod{width:114px;height:190px;background:#fff}
.prod-img{left:0;top:0;width:114px;height:110px}
.prod-name{left:7px;top:118px;font-size:8px;color:#333}
.prod-price{left:7px;top:134px;font-size:9px;font-weight:700}
.prod-rate{right:7px;top:134px;font-size:8px;color:#999}
.prod-rate b{position:static!important;color:var(--star);font-weight:400}
.btn-cart{left:7px;top:165px;width:70px;height:16px;background:var(--navy);color:#fff;font-size:6px;text-align:center;line-height:16px}
.btn-fav{left:86px;top:165px;width:20px;height:16px;border:1px solid var(--accent);color:var(--accent);font-size:10px;text-align:center;line-height:13px;background:#fff}
.img-navy{background:linear-gradient(140deg,#eeeeee 18%,#c4925e 38%,#2d3a66 60%,#c9a873 72%,#eeeeee 86%)}
.img-lace{background:linear-gradient(140deg,#eeeeee 16%,#d49a64 40%,#c9a77a 58%,#b98a5a 72%,#eeeeee 88%)}
.img-wine{background:linear-gradient(140deg,#eeeeee 18%,#c89568 36%,#8d2f46 58%,#a23b52 70%,#eeeeee 86%)}
.img-gold{background:linear-gradient(140deg,#eeeeee 18%,#d19a64 40%,#8f6b2c 58%,#b18845 70%,#eeeeee 86%)}

.popular-band{left:0;top:893px;width:720px;height:308px;background:var(--soft)}

.cust-title{font-size:32px;font-weight:300;color:#222}
.cust-sub{font-size:12px;line-height:14px;color:#222;white-space:normal!important;width:250px}
.paper{width:70px;height:110px}
.form-box{width:225px;height:174px}
.form-head{left:26px;top:14px;font-size:9.5px;color:#333}
.field{left:26px;width:172px;height:22px;background:#fff;font-size:6.5px;color:#888;padding:7px 8px}
.btn-send{left:26px;width:64px;height:16px;background:var(--navy);color:#fff;font-size:6px;text-align:center;line-height:16px}
.photo{border:6px solid #fff;box-shadow:0 2px 8px rgba(0,0,0,.2)}
.tape{width:34px;height:12px;background:rgba(220,220,220,.85)}

.about-band{left:0;top:1678px;width:720px;height:200px;background:var(--aqua)}
.about-img{left:0;top:0;width:258px;height:200px;background:linear-gradient(120deg,#d8d1c4,#8f7a62 45%,#4a4a52 70%,#b7ad9c)}
.about-title{left:312px;top:36px;font-size:24px;font-weight:300}
.about-text{left:312px;top:76px;width:320px;font-size:11.5px;line-height:14.5px;color:#222;white-space:normal!important}

.foot-line{left:27px;width:665px;height:1px;background:var(--line)}
.foot{left:0;width:720px;height:200px}
.foot-h{font-size:9.5px;color:#222}
.foot-i{font-size:7.5px;color:#555}
.foot-c{font-size:7px;color:#888}
.soc{width:9px;height:9px;border-radius:50%;background:#222}
.pay{width:36px;height:16px;font-size:7px;font-weight:600;color:var(--navy);line-height:16px;text-align:center}
.ico{width:10px;height:10px}

.banner{left:30px;top:76px;width:640px;height:160px;background:var(--cream);box-shadow:0 0 18px rgba(240,220,170,.6)}
.banner-title{left:26px;top:64px;font-family:"Playfair Display",serif;font-size:26px;font-weight:700;color:#111}
.banner-photo{left:395px;top:17px;width:212px;height:128px;border:4px solid #fff;background:linear-gradient(120deg,#c9b8a4,#8fa3b8 35%,#dcc7ae 60%,#6d7f97 85%)}
.sort-l{left:577px;top:345px;font-size:7.5px}
.sort{left:610px;top:341px;width:72px;height:18px;border:1px solid #ddd;font-size:6.5px;color:#666;padding:5px 10px}
.sort::after{content:"";position:absolute;right:7px;top:6px;border-left:4px solid transparent;border-right:4px solid transparent;border-top:5px solid #222}
.side{left:40px;top:388px;width:150px;height:188px;background:var(--lilac);box-shadow:0 1px 3px rgba(0,0,0,.08)}
.side-head{left:0;top:0;width:150px;height:26px;background:#fff;font-size:7.5px;font-weight:500;padding:9px 10px}
.side-sub{left:10px;top:34px;font-size:7px;font-weight:700}
.opt{left:10px;font-size:6.5px;color:#333;padding-left:15px}
.opt::before{content:"";position:absolute;left:0;top:0;width:9px;height:9px;border:1px solid #777;background:#fff}
.opt.on::before{background:#f09a86;border-color:#f09a86}
.pager{top:1014px;font-size:6.5px;color:#999}
.pbox{top:1011px;width:12px;height:11px;border:1px solid #ccc;font-size:6.5px;text-align:center;line-height:9px;color:#333}
.cust-band{left:0;top:1044px;width:720px;height:200px;background:var(--sand)}
</style>
</head>
<body>
<div class="stage">
  <p class="stage-title" style="left:405px">Homepage</p>
  <p class="stage-title" style="left:1158px">Product Category Page</p>

  <!-- HOMEPAGE -->
  <section class="page" style="left:45px;top:92px;height:2108px">
    <p class="logo">Lovmira</p>
    <span class="nav" style="left:40px">Home</span>
    <span class="nav" style="left:88px">Products<i class="nav-caret"></i></span>
    <span class="nav" style="left:165px">News</span>
    <span class="nav" style="left:212px">About Us</span>
    <span class="nav" style="left:273px">Contact Us</span>
    <span class="nav" style="left:343px">Send Inquiry</span>
    <svg class="search" viewBox="0 0 12 12"><circle cx="5" cy="5" r="4" fill="none" stroke="#333" stroke-width="1.2"/><line x1="8" y1="8" x2="11" y2="11" stroke="#333" stroke-width="1.2"/></svg>
    <span class="search-text">Search</span>
    <svg class="hicon" style="left:613px" viewBox="0 0 12 12"><circle cx="6" cy="6" r="5" fill="none" stroke="#333"/><circle cx="6" cy="5" r="2" fill="#333"/></svg>
    <svg class="hicon" style="left:639px" viewBox="0 0 12 12"><path d="M6 10.5 1.5 6A2.5 2.5 0 0 1 6 3a2.5 2.5 0 0 1 4.5 3z" fill="none" stroke="#333"/><circle cx="10" cy="2" r="2" fill="#e0612b"/></svg>
    <svg class="hicon" style="left:665px" viewBox="0 0 12 12"><path d="M1 2h2l1.5 6h5.5l1-4H4" fill="none" stroke="#333"/><circle cx="5" cy="10.5" r="1" fill="#333"/><circle cx="9" cy="10.5" r="1" fill="#333"/><circle cx="10" cy="2" r="2" fill="#e0612b"/></svg>
    <div class="header-line"></div>

    <div class="hero" role="img" aria-label="Bride and groom embracing under a veil with white orchids"></div>
    <p class="hero-title">Celebrate Your Moment with Your Beloved Ones</p>
    <p class="hero-sub">We provide a unique mesmerizing invitation for your event</p>
    <span class="btn-buy">BUY NOW</span>
    <div class="arrow l" style="left:26px;top:232px"></div>
    <div class="arrow r" style="left:676px;top:232px"></div>
    <div class="dot" style="left:340px"></div><div class="dot on" style="left:351px"></div><div class="dot" style="left:362px"></div><div class="dot" style="left:373px"></div>

    <p class="section-title" style="top:459px">Explore Categories</p>
    <div class="chip" style="left:38px;top:498px"><div class="chip-icon" style="background:#e9a6a0"></div><p class="chip-text">Wedding Invitation Card</p></div>
    <div class="chip" style="left:147px;top:498px"><div class="chip-icon" style="background:#d9833f"></div><p class="chip-text">3D Pop Up Card</p></div>
    <div class="chip" style="left:256px;top:498px"><div class="chip-icon" style="background:#9cc6d8"></div><p class="chip-text">Greeting Card</p></div>
    <div class="chip" style="left:365px;top:498px"><div class="chip-icon" style="background:#e79a8c"></div><p class="chip-text">Wedding Stationery</p></div>
    <div class="chip" style="left:474px;top:498px"><div class="chip-icon" style="background:#f2c65a"></div><p class="chip-text">Wedding Decoration Accessories</p></div>
    <div class="chip" style="left:583px;top:498px"><div class="chip-icon" style="background:#8fd0b0"></div><p class="chip-text">Laser Cut Favor Box</p></div>

    <p class="section-title" style="top:610px">Our Collections</p>
    <div class="coll" style="left:40px"><div class="coll-img img-wine" role="img" aria-label="Burgundy pocket invitation with kraft envelope"></div><div class="coll-band"><p class="coll-name">POCKET CARD</p><p class="coll-link">View All</p></div></div>
    <div class="coll" style="left:202px"><div class="coll-img" role="img" aria-label="Vintage lace and burlap invitation" style="background:linear-gradient(140deg,#eeeeee 15%,#cbbfae 35%,#b7a88f 60%,#eeeeee 85%)"></div><div class="coll-band"><p class="coll-name">VINTAGE CARD</p><p class="coll-link">View All</p></div></div>
    <div class="coll" style="left:364px"><div class="coll-img" role="img" aria-label="Navy 3D pop up wedding card" style="background:linear-gradient(140deg,#eeeeee 18%,#253058 40%,#cfd2dc 58%,#253058 75%,#eeeeee 88%)"></div><div class="coll-band"><p class="coll-name">POP UP CARD</p><p class="coll-link">View All</p></div></div>
    <div class="coll" style="left:526px"><div class="coll-img img-lace" role="img" aria-label="Laser cut lace invitation on kraft envelope"></div><div class="coll-band"><p class="coll-name">LASER CUTTING CARD</p><p class="coll-link">View All</p></div></div>

    <div class="popular-band"></div>
    <p class="section-title" style="top:950px">Popular Cards</p>
    <div class="prod" style="left:58px;top:988px"><div class="prod-img img-navy" role="img" aria-label="Navy laser cut invitation"></div><p class="prod-name">Product Name</p><p class="prod-price">$2.4</p><span class="prod-rate"><b>★</b> (4.9)</span><span class="btn-cart">Add to Cart</span><span class="btn-fav">♡</span></div>
    <div class="prod" style="left:180px;top:988px"><div class="prod-img img-lace" role="img" aria-label="Kraft lace invitation"></div><p class="prod-name">Amber Lacewing</p><p class="prod-price">$2.4</p><span class="prod-rate"><b>★</b> (4.8)</span><span class="btn-cart">Add to Cart</span><span class="btn-fav">♥</span></div>
    <div class="prod" style="left:302px;top:988px"><div class="prod-img img-wine" role="img" aria-label="Burgundy pocket invitation"></div><p class="prod-name">Velvet Ribbon</p><p class="prod-price">$2.4</p><span class="prod-rate"><b>★</b> (4.9)</span><span class="btn-cart">Add to Cart</span><span class="btn-fav">♡</span></div>
    <div class="prod" style="left:424px;top:988px"><div class="prod-img img-gold" role="img" aria-label="Gold lace invitation"></div><p class="prod-name">Golden Vow</p><p class="prod-price">$2.4</p><span class="prod-rate"><b>★</b> (4.9)</span><span class="btn-cart">Add to Cart</span><span class="btn-fav">♡</span></div>
    <div class="prod" style="left:548px;top:988px"><div class="prod-img img-gold" role="img" aria-label="Gold lace invitation"></div><p class="prod-name">Golden Vow</p><p class="prod-price">$2.4</p><span class="prod-rate"><b>★</b> (4.9)</span><span class="btn-cart">Add to Cart</span><span class="btn-fav">♡</span></div>
    <div class="arrow hot l" style="left:21px;top:1071px"></div>
    <div class="arrow hot r" style="left:672px;top:1071px"></div>

    <p class="cust-title" style="left:67px;top:1288px">Customize Your Card</p>
    <p class="cust-sub" style="left:71px;top:1329px">Have your own design ? or want something to be more special ?</p>
    <div class="paper" style="left:80px;top:1410px;background:#a9c3cc;transform:rotate(14deg)"></div>
    <div class="paper" style="left:110px;top:1440px;background:#f8cbb0;transform:rotate(-6deg)"></div>
    <div class="form-box" style="left:132px;top:1376px;background:var(--sand)">
      <p class="form-head">Let’s talk more about what you need</p>
      <p class="field" style="top:34px">Your Name</p>
      <p class="field" style="top:62px">Your Phone Number/E-mail</p>
      <p class="field" style="top:90px;height:46px">Message</p>
      <span class="btn-send" style="top:145px">Send</span>
    </div>
    <div class="photo" role="img" aria-label="Smiling couple photo" style="left:415px;top:1345px;width:120px;height:112px;transform:rotate(-8deg);background:linear-gradient(130deg,#d8c3a8,#a98b6e 50%,#e6dccd)"></div>
    <div class="tape" style="left:405px;top:1342px;transform:rotate(-40deg)"></div>
    <div class="tape" style="left:505px;top:1340px;transform:rotate(40deg)"></div>
    <div class="photo" role="img" aria-label="Party guests celebrating photo" style="left:567px;top:1350px;width:112px;height:112px;transform:rotate(8deg);background:linear-gradient(130deg,#6f5a4c,#c9a15d 45%,#3b3540 80%)"></div>
    <div class="tape" style="left:568px;top:1343px;transform:rotate(-35deg)"></div>
    <div class="tape" style="left:650px;top:1350px;transform:rotate(40deg)"></div>
    <div class="photo" role="img" aria-label="Friends picnic gathering photo" style="left:485px;top:1478px;width:122px;height:110px;transform:rotate(-12deg);background:linear-gradient(130deg,#cfa27a,#8ea4a8 45%,#d77c55 80%)"></div>
    <div class="tape" style="left:480px;top:1478px;transform:rotate(-40deg)"></div>
    <div class="tape" style="left:575px;top:1476px;transform:rotate(35deg)"></div>

    <div class="about-band">
      <div class="about-img" role="img" aria-label="Team working together in a library office"></div>
      <p class="about-title">About Us</p>
      <p class="about-text">Lorem ipsum dolor sit amet, consectetur adipiscing elit. Interdum convallis risus eget scelerisque. Massa quis tellus adipiscing ac vel, id vitae, leo. Quis mattis vestib morbi commodo. Eget consequat, pellentes adipiscing eu fringilla at. Eget eget tempus consectetur urna orci amet. Tellus ultrices et tempus lectus etiam.</p>
    </div>

    <div class="foot-line" style="top:1911px"></div>
    <div class="foot" style="top:1968px">
      <p class="foot-h" style="left:47px;top:0">About</p>
      <svg class="ico" style="left:48px;top:21px" viewBox="0 0 10 10"><path d="M5 9.5C2 6 2 5 2 4a3 3 0 0 1 6 0c0 1 0 2-3 5.5z" fill="none" stroke="#777"/><circle cx="5" cy="4" r="1" fill="#777"/></svg>
      <p class="foot-c" style="left:63px;top:22px">Harbor Lane, Portvale, 40218</p>
      <svg class="ico" style="left:48px;top:47px" viewBox="0 0 10 10"><path d="M2 1h2l1 2.5-1.2 1a5 5 0 0 0 2.7 2.7l1-1.2L9 7v2C5 9 1 5 1 1z" fill="none" stroke="#777"/></svg>
      <p class="foot-c" style="left:63px;top:48px">01 2345 6789</p>
      <svg class="ico" style="left:48px;top:65px" viewBox="0 0 10 10"><rect x="1" y="2" width="8" height="6" fill="none" stroke="#777"/><path d="M1 2l4 3.5L9 2" fill="none" stroke="#777"/></svg>
      <p class="foot-c" style="left:63px;top:66px">Admin@bluestonecraft.com</p>
      <p class="foot-h" style="left:252px;top:0">Quick Access</p>
      <p class="foot-i" style="left:252px;top:20px">Home</p><p class="foot-i" style="left:252px;top:35.5px">Products</p><p class="foot-i" style="left:252px;top:51px">News</p><p class="foot-i" style="left:252px;top:66.5px">About Us</p><p class="foot-i" style="left:252px;top:82px">Contact Us</p><p class="foot-i" style="left:252px;top:97.5px">Send Inquiry</p>
      <p class="foot-h" style="left:341px;top:0">Category</p>
      <p class="foot-i" style="left:341px;top:20px">Wedding Invitation Card</p><p class="foot-i" style="left:341px;top:35.5px">3D Pop Up Card</p><p class="foot-i" style="left:341px;top:51px">Greeting Card</p><p class="foot-i" style="left:341px;top:66.5px">Wedding Stationary</p><p class="foot-i" style="left:341px;top:82px">Wedding Decoration</p><p class="foot-i" style="left:341px;top:97.5px">Laser Cut Favor Box</p>
      <p class="foot-h" style="left:456px;top:0">Share</p>
      <span class="soc" style="left:458px;top:20px"></span><span class="soc" style="left:476px;top:20px"></span><span class="soc" style="left:494px;top:20px"></span><span class="soc" style="left:512px;top:20px"></span>
      <p class="foot-h" style="left:554px;top:0">Payment Methods</p>
      <span class="pay" style="left:552px;top:20px">Zarvique</span><span class="pay" style="left:590px;top:20px">Plenmo</span><span class="pay" style="left:628px;top:20px">Quelvo</span>
      <span class="pay" style="left:552px;top:42px">Tindrix</span><span class="pay" style="left:590px;top:42px">Marobel</span>
    </div>
  </section>

  <!-- CATEGORY PAGE -->
  <section class="page" style="left:785px;top:92px;height:1474px">
    <p class="logo">Lovmira</p>
    <span class="nav" style="left:40px">Home</span>
    <span class="nav" style="left:88px">Products<i class="nav-caret"></i></span>
    <span class="nav" style="left:165px">News</span>
    <span class="nav" style="left:212px">About Us</span>
    <span class="nav" style="left:273px">Contact Us</span>
    <span class="nav" style="left:343px">Send Inquiry</span>
    <svg class="search" viewBox="0 0 12 12"><circle cx="5" cy="5" r="4" fill="none" stroke="#333" stroke-width="1.2"/><line x1="8" y1="8" x2="11" y2="11" stroke="#333" stroke-width="1.2"/></svg>
    <span class="search-text">Search</span>
    <svg class="hicon" style="left:613px" viewBox="0 0 12 12"><circle cx="6" cy="6" r="5" fill="none" stroke="#333"/><circle cx="6" cy="5" r="2" fill="#333"/></svg>
    <svg class="hicon" style="left:639px" viewBox="0 0 12 12"><path d="M6 10.5 1.5 6A2.5 2.5 0 0 1 6 3a2.5 2.5 0 0 1 4.5 3z" fill="none" stroke="#333"/><circle cx="10" cy="2" r="2" fill="#e0612b"/></svg>
    <svg class="hicon" style="left:665px" viewBox="0 0 12 12"><path d="M1 2h2l1.5 6h5.5l1-4H4" fill="none" stroke="#333"/><circle cx="5" cy="10.5" r="1" fill="#333"/><circle cx="9" cy="10.5" r="1" fill="#333"/><circle cx="10" cy="2" r="2" fill="#e0612b"/></svg>
    <div class="header-line"></div>

    <div class="banner">
      <p class="banner-title">Wedding Invitation Card</p>
      <div class="banner-photo" role="img" aria-label="Wedding party group photo outdoors"></div>
    </div>

    <div class="chip on" style="left:38px;top:260px"><div class="chip-icon" style="background:#fff"></div><p class="chip-text">Wedding Invitation Card</p></div>
    <div class="chip" style="left:147px;top:260px"><div class="chip-icon" style="background:#d9833f"></div><p class="chip-text">3D Pop Up Card</p></div>
    <div class="chip" style="left:256px;top:260px"><div class="chip-icon" style="background:#9cc6d8"></div><p class="chip-text">Greeting Card</p></div>
    <div class="chip" style="left:365px;top:260px"><div class="chip-icon" style="background:#e79a8c"></div><p class="chip-text">Wedding Stationery</p></div>
    <div class="chip" style="left:474px;top:260px"><div class="chip-icon" style="background:#f2c65a"></div><p class="chip-text">Wedding Decoration Accessories</p></div>
    <div class="chip" style="left:583px;top:260px"><div class="chip-icon" style="background:#8fd0b0"></div><p class="chip-text">Laser Cut Favor Box</p></div>

    <span class="sort-l">Set by</span>
    <span class="sort">Popularity</span>

    <div class="side">
      <p class="side-head">CATEGORY</p>
      <p class="side-sub">WEDDING INVITATION CARD</p>
      <p class="opt on" style="top:52px">All</p>
      <p class="opt" style="top:66px">Laser cut wedding invitation</p>
      <p class="opt" style="top:80px">Popup wedding invitation</p>
      <p class="opt" style="top:94px">Vintage wedding invitation</p>
      <p class="opt" style="top:108px">Handmade wedding invitation</p>
      <p class="opt" style="top:122px">Pocket wedding invitation</p>
      <p class="opt" style="top:136px">Handmade wedding invitation</p>
      <p class="opt" style="top:150px">Acrylic wedding invitation</p>
      <p class="opt" style="top:164px">Custom wedding invitation</p>
    </div>

    <div class="prod" style="left:202px;top:388px"><div class="prod-img img-navy" role="img" aria-label="Navy laser cut invitation"></div><p class="prod-name">Product Name</p><p class="prod-price">$2.4</p><span class="prod-rate"><b>★</b> (4.9)</span><span class="btn-cart">Add to Cart</span><span class="btn-fav">♡</span></div>
    <div class="prod" style="left:324px;top:388px"><div class="prod-img img-lace" role="img" aria-label="Kraft lace invitation"></div><p class="prod-name">Amber Lacewing</p><p class="prod-price">$2.4</p><span class="prod-rate"><b>★</b> (4.9)</span><span class="btn-cart">Add to Cart</span><span class="btn-fav">♥</span></div>
    <div class="prod" style="left:446px;top:388px"><div class="prod-img img-wine" role="img" aria-label="Burgundy pocket invitation"></div><p class="prod-name">Velvet Ribbon</p><p class="prod-price">$2.4</p><span class="prod-rate"><b>★</b> (4.9)</span><span class="btn-cart">Add to Cart</span><span class="btn-fav">♡</span></div>
    <div class="prod" style="left:568px;top:388px"><div class="prod-img img-gold" role="img" aria-label="Gold lace invitation"></div><p class="prod-name">Golden Vow</p><p class="prod-price">$2.4</p><span class="prod-rate"><b>★</b> (4.9)</span><span class="btn-cart">Add to Cart</span><span class="btn-fav">♡</span></div>

    <div class="prod" style="left:202px;top:593px"><div class="prod-img img-navy" role="img" aria-label="Navy laser cut invitation"></div><p class="prod-name">Product Name</p><p class="prod-price">$2.4</p><span class="prod-rate"><b>★</b> (4.9)</span><span class="btn-cart">Add to Cart</span><span class="btn-fav">♡</span></div>
    <div class="prod" style="left:324px;top:593px"><div class="prod-img img-lace" role="img" aria-label="Kraft lace invitation"></div><p class="prod-name">Amber Lacewing</p><p class="prod-price">$2.4</p><span class="prod-rate"><b>★</b> (4.9)</span><span class="btn-cart">Add to Cart</span><span class="btn-fav">♥</span></div>
    <div class="prod" style="left:446px;top:593px"><div class="prod-img img-wine" role="img" aria-label="Burgundy pocket invitation"></div><p class="prod-name">Velvet Ribbon</p><p class="prod-price">$2.4</p><span class="prod-rate"><b>★</b> (4.9)</span><span class="btn-cart">Add to Cart</span><span class="btn-fav">♡</span></div>
    <div class="prod" style="left:568px;top:593px"><div class="prod-img img-gold" role="img" aria-label="Gold lace invitation"></div><p class="prod-name">Golden Vow</p><p class="prod-price">$2.4</p><span class="prod-rate"><b>★</b> (4.9)</span><span class="btn-cart">Add to Cart</span><span class="btn-fav">♡</span></div>

    <div class="prod" style="left:202px;top:798px"><div class="prod-img img-navy" role="img" aria-label="Navy laser cut invitation"></div><p class="prod-name">Product Name</p><p class="prod-price">$2.4</p><span class="prod-rate"><b>★</b> (4.9)</span><span class="btn-cart">Add to Cart</span><span class="btn-fav">♡</span></div>
    <div class="prod" style="left:324px;top:798px"><div class="prod-img img-lace" role="img" aria-label="Kraft lace invitation"></div><p class="prod-name">Amber Lacewing</p><p class="prod-price">$2.4</p><span class="prod-rate"><b>★</b> (4.9)</span><span class="btn-cart">Add to Cart</span><span class="btn-fav">♥</span></div>
    <div class="prod" style="left:446px;top:798px"><div class="prod-img img-wine" role="img" aria-label="Burgundy pocket invitation"></div><p class="prod-name">Velvet Ribbon</p><p class="prod-price">$2.4</p><span class="prod-rate"><b>★</b> (4.9)</span><span class="btn-cart">Add to Cart</span><span class="btn-fav">♡</span></div>
    <div class="prod" style="left:568px;top:798px"><div class="prod-img img-gold" role="img" aria-label="Gold lace invitation"></div><p class="prod-name">Golden Vow</p><p class="prod-price">$2.4</p><span class="prod-rate"><b>★</b> (4.9)</span><span class="btn-cart">Add to Cart</span><span class="btn-fav">♡</span></div>

    <span class="pager" style="left:570px">Page</span>
    <span class="pbox" style="left:593px;width:18px">10</span>
    <span class="pager" style="left:618px">of 50</span>
    <span class="pbox" style="left:645px">‹</span>
    <span class="pbox" style="left:662px">›</span>

    <div class="cust-band">
      <p class="cust-title" style="left:67px;top:16px;font-size:28px">Customize Your Card</p>
      <p class="cust-sub" style="left:71px;top:56px">Have your own design ? or want something to be more special ?</p>
      <div class="photo" role="img" aria-label="Smiling couple photo" style="left:60px;top:110px;width:120px;height:110px;transform:rotate(-10deg);background:linear-gradient(130deg,#d8c3a8,#a98b6e 50%,#e6dccd)"></div>
      <div class="photo" role="img" aria-label="Party guests celebrating photo" style="left:200px;top:92px;width:112px;height:120px;transform:rotate(8deg);background:linear-gradient(130deg,#6f5a4c,#c9a15d 45%,#3b3540 80%)"></div>
      <div class="tape" style="left:200px;top:86px;transform:rotate(-35deg)"></div>
      <div class="tape" style="left:286px;top:92px;transform:rotate(40deg)"></div>
      <div class="paper" style="left:385px;top:40px;background:#a9c3cc;transform:rotate(14deg)"></div>
      <div class="paper" style="left:415px;top:70px;background:#f8cbb0;transform:rotate(-6deg)"></div>
      <div class="form-box" style="left:435px;top:12px;background:var(--butter)">
        <p class="form-head">Let’s talk more about what you need</p>
        <p class="field" style="top:34px">Your Name</p>
        <p class="field" style="top:62px">Your Phone Number/E-mail</p>
        <p class="field" style="top:90px;height:46px">Message</p>
        <span class="btn-send" style="top:145px">Send</span>
      </div>
    </div>

    <div class="foot-line" style="top:1274px"></div>
    <div class="foot" style="top:1333px">
      <p class="foot-h" style="left:47px;top:0">About</p>
      <svg class="ico" style="left:48px;top:21px" viewBox="0 0 10 10"><path d="M5 9.5C2 6 2 5 2 4a3 3 0 0 1 6 0c0 1 0 2-3 5.5z" fill="none" stroke="#777"/><circle cx="5" cy="4" r="1" fill="#777"/></svg>
      <p class="foot-c" style="left:63px;top:22px">Harbor Lane, Portvale, 40218</p>
      <svg class="ico" style="left:48px;top:47px" viewBox="0 0 10 10"><path d="M2 1h2l1 2.5-1.2 1a5 5 0 0 0 2.7 2.7l1-1.2L9 7v2C5 9 1 5 1 1z" fill="none" stroke="#777"/></svg>
      <p class="foot-c" style="left:63px;top:48px">01 2345 6789</p>
      <svg class="ico" style="left:48px;top:65px" viewBox="0 0 10 10"><rect x="1" y="2" width="8" height="6" fill="none" stroke="#777"/><path d="M1 2l4 3.5L9 2" fill="none" stroke="#777"/></svg>
      <p class="foot-c" style="left:63px;top:66px">Admin@bluestonecraft.com</p>
      <p class="foot-h" style="left:252px;top:0">Quick Access</p>
      <p class="foot-i" style="left:252px;top:20px">Home</p><p class="foot-i" style="left:252px;top:35.5px">Products</p><p class="foot-i" style="left:252px;top:51px">News</p><p class="foot-i" style="left:252px;top:66.5px">About Us</p><p class="foot-i" style="left:252px;top:82px">Contact Us</p><p class="foot-i" style="left:252px;top:97.5px">Send Inquiry</p>
      <p class="foot-h" style="left:341px;top:0">Category</p>
      <p class="foot-i" style="left:341px;top:20px">Wedding Invitation Card</p><p class="foot-i" style="left:341px;top:35.5px">3D Pop Up Card</p><p class="foot-i" style="left:341px;top:51px">Greeting Card</p><p class="foot-i" style="left:341px;top:66.5px">Wedding Stationary</p><p class="foot-i" style="left:341px;top:82px">Wedding Decoration</p><p class="foot-i" style="left:341px;top:97.5px">Laser Cut Favor Box</p>
      <p class="foot-h" style="left:456px;top:0">Share</p>
      <span class="soc" style="left:458px;top:20px"></span><span class="soc" style="left:476px;top:20px"></span><span class="soc" style="left:494px;top:20px"></span><span class="soc" style="left:512px;top:20px"></span>
      <p class="foot-h" style="left:554px;top:0">Payment Methods</p>
      <span class="pay" style="left:552px;top:20px">Zarvique</span><span class="pay" style="left:590px;top:20px">Plenmo</span><span class="pay" style="left:628px;top:20px">Quelvo</span>
      <span class="pay" style="left:552px;top:42px">Tindrix</span><span class="pay" style="left:590px;top:42px">Marobel</span>
    </div>
  </section>
</div>
</body>
</html>
```